Business Card Design

It's an investment advisory service for individuals with all there investment needs. Also financial consulting to businesses and governmental agencies on retirement plans etc. It's personalized not commoditized help. Should show strength, knowledge and money orientation.

Industry/Entity Type

Investment

Contact Information for Business Card

B. Vel R. Financial Consulting and Wealth Management, Mirek Dale Hopstein, 5172 Paseo Las Colinas Verde, San Diego, CA 92084-6617, Registered Investment Advisor

Requirements
Nice to have
• Something money oriented

```html
<!DOCTYPE html>
<html lang="en">
<head>
<meta charset="utf-8">
<title>B. Vel R. Financial Consulting – Business Card</title>
<link rel="stylesheet" href="https://fonts.googleapis.com/css2?family=Ubuntu:wght@400;500;700&display=swap">
<style>
  :root {
    --backdrop: #e6e6e4;
    --card-white: #f4f4f2;
    --brand-green: #4cb52a;
    --brand-green-dark: #3f9c22;
    --ink: #3d3d3d;
    --on-green: #ffffff;
    --money-light: #efeee2;
    --money-mid: #d9dcc4;
  }
  * { box-sizing: border-box; margin: 0; padding: 0; }
  html, body {
    width: 1200px; height: 1000px; overflow: hidden;
    background: var(--backdrop);
    font-family: "Ubuntu", sans-serif;
  }
  .canvas {
    position: relative; width: 1200px; height: 1000px;
    display: flex; align-items: center; justify-content: center;
  }
  .business-card {
    position: relative; width: 900px; height: 514px;
    background: var(--card-white);
    box-shadow: 0 10px 30px rgba(0,0,0,0.18);
    overflow: hidden;
  }
  .brand-side {
    position: absolute; left: 0; top: 0; width: 420px; height: 100%;
  }
  .money-photo {
    position: absolute; left: 270px; top: 70px; width: 150px; height: 290px;
    background: linear-gradient(90deg, rgba(239,238,226,0) 0%, var(--money-light) 35%, var(--money-mid) 100%);
  }
  .brand-mark {
    position: absolute; left: 70px; top: 150px;
    display: flex; flex-direction: column; align-items: flex-end;
  }
  .brand-name {
    display: flex; align-items: center; gap: 12px;
    font-size: 34px; font-weight: 700; color: var(--brand-green);
    margin-bottom: 12px; align-self: flex-start; margin-left: 40px;
  }
  .brand-dot {
    width: 26px; height: 26px; border-radius: 50%;
    background: var(--brand-green);
  }
  .brand-tagline {
    font-size: 27px; font-weight: 400; color: var(--ink);
    line-height: 1.12; text-align: right;
  }
  .contact-side {
    position: absolute; left: 420px; top: 0; width: 480px; height: 100%;
    background: var(--brand-green);
    color: var(--on-green);
    padding: 108px 0 0 52px;
  }
  .person-name { font-size: 33px; font-weight: 700; letter-spacing: 0.2px; }
  .person-title { font-size: 19px; font-weight: 400; margin-top: 4px; }
  .contact-icons { display: flex; gap: 12px; margin-top: 34px; }
  .contact-icon {
    width: 38px; height: 38px; border-radius: 50%;
    background: var(--on-green);
    display: flex; align-items: center; justify-content: center;
  }
  .contact-icon svg { width: 22px; height: 22px; fill: var(--brand-green); }
  .address { font-size: 25px; line-height: 1.3; margin-top: 18px; }
</style>
</head>
<body>
<main class="canvas">
  <article class="business-card">
    <section class="brand-side">
      <div class="money-photo" role="img" aria-label="Photograph of stacked dollar bill bundles, fading into the white background"></div>
      <div class="brand-mark">
        <div class="brand-name"><span class="brand-dot"></span>B. Vel R.</div>
        <p class="brand-tagline">Financial Consulting<br>and Wealth Management</p>
      </div>
    </section>
    <section class="contact-side">
      <h1 class="person-name">Mirek Dale Hopstein</h1>
      <p class="person-title">Investment Advisor</p>
      <div class="contact-icons">
        <span class="contact-icon" aria-label="Address">
          <svg viewBox="0 0 24 24"><path d="M12 3 2 12h3v8h5v-5h4v5h5v-8h3z"/></svg>
        </span>
        <span class="contact-icon" aria-label="Phone">
          <svg viewBox="0 0 24 24"><path d="M6.6 10.8a15.1 15.1 0 0 0 6.6 6.6l2.2-2.2c.3-.3.7-.4 1-.2 1.1.4 2.3.6 3.6.6.6 0 1 .4 1 1V20c0 .6-.4 1-1 1A17 17 0 0 1 3 4c0-.6.4-1 1-1h3.5c.6 0 1 .4 1 1 0 1.3.2 2.5.6 3.6.1.3 0 .7-.2 1z"/></svg>
        </span>
        <span class="contact-icon" aria-label="Email">
          <svg viewBox="0 0 24 24"><path d="M3 6h18v12H3z M3 6l9 7 9-7" fill="none" stroke="#4cb52a" stroke-width="2" stroke-linejoin="round"/></svg>
        </span>
      </div>
      <p class="address">5172 Paseo Las Colinas Verde<br>San Diego, CA 92084-6617</p>
    </section>
  </article>
</main>
</body>
</html>
```